Website Home Page for Women's Health Medical Office

Redesign existing homepage for website using existing logo. Current website location is www.larkfieldwomenscare.com. Please give it a modern, streamlined, playful feel.

Please give it a feminine feel and make it bright and cheerful using logo colors.

Target Market(s)

Women between the ages of 25-45

Industry/Entity Type

Medical Office

Coding

Coded - Design and coding required

Number of Pages Required

1 page

Font styles to use
Sans Serif
Other font styles liked:
• SEGOI UI script for text and GIL SANS for bold (or their equivilent)

Colors
E54698
E96AAD
F1A4CE
F9D9EA
FCEFF6

Requirements
Must have
• Existing logo. Logo Colors. Feminine, cheerful, simple design. all relevant contact information
Nice to have
• clean lines and streamlined look
Should not have
• Cluttered

```html
<!DOCTYPE html>
<html lang="en">
<head>
<meta charset="utf-8">
<title>Larkfield OB/GYN – Home</title>
<link rel="stylesheet" href="https://fonts.googleapis.com/css2?family=Josefin+Sans:wght@400;500;600&family=Nunito+Sans:wght@400;600;700&display=swap">
<style>
:root{
  --hot:#F5168A;
  --pink:#E54698;
  --pink-2:#E96AAD;
  --pink-3:#F1A4CE;
  --pink-4:#F9D9EA;
  --pink-5:#FCEFF6;
  --ink:#222;
  --ink-soft:#3a3a3a;
  --slate:#4a4a4a;
  --mist:#e2e2e2;
}
*{margin:0;padding:0;box-sizing:border-box}
html,body{width:1200px;height:3606px;overflow:hidden}
body{position:relative;background:#fff;font-family:"Nunito Sans",sans-serif;color:var(--ink)}
.abs{position:absolute}
.head{font-family:"Josefin Sans",sans-serif;color:var(--hot);font-weight:500}

/* header */
.topbar{left:0;top:0;width:1200px;height:127px;background:#fff}
.brand{left:75px;top:38px;display:flex;align-items:center;gap:14px}
.brand-name{font-family:"Josefin Sans",sans-serif;font-weight:600;font-size:28px;color:var(--ink)}
.brand-dot{width:40px;height:40px;border-radius:50%;background:var(--pink-4)}
.contact{top:52px;display:flex;gap:7px;font-size:12.5px;line-height:16px;white-space:nowrap}
.contact small{display:block;color:var(--hot);font-size:10.5px}
.contact svg{flex:none;margin-top:2px}
.nav{left:0;top:127px;width:1200px;height:87px;background:var(--hot)}
.nav a{position:absolute;top:26px;color:#fff;font-size:20px;text-decoration:none;font-family:"Josefin Sans",sans-serif}
.book{left:845px;top:148px;width:237px;height:46px;background:#fff;border-radius:10px;color:var(--hot);font-size:20px;display:flex;align-items:center;justify-content:center;font-family:"Josefin Sans",sans-serif;letter-spacing:.3px}

/* hero */
.hero{left:0;top:214px;width:1200px;height:620px;background:var(--pink-5);overflow:hidden}
.hero h1{left:133px;top:128px;font-size:42px;line-height:56px;font-weight:500}
.hero p{left:138px;top:262px;font-size:19px;line-height:27px;width:400px}
.photo{background:linear-gradient(165deg,#FDF5FA,var(--pink-4))}

/* intro */
.intro-ring{left:180px;top:895px;width:337px;height:435px;border:1.5px solid var(--hot);border-radius:170px}
.intro-photo{left:193px;top:915px;width:312px;height:397px;border-radius:156px}
.intro h2{left:623px;top:902px;font-size:30px;line-height:40px}
.body-copy{font-size:14.2px;line-height:20px;color:var(--ink-soft)}
.body-copy p+p{margin-top:20px}

/* banner */
.banner{left:138px;top:1405px;width:922px;height:255px;border-radius:24px;background:linear-gradient(100deg,var(--pink-4),var(--pink-5) 60%,#fff)}
.banner .eyebrow{left:91px;top:57px;font-size:19px}
.banner h3{left:91px;top:88px;font-size:29px;color:var(--ink);font-weight:400;font-family:"Josefin Sans",sans-serif}
.banner .cta{left:91px;top:148px;font-size:20px;line-height:28px;font-family:"Josefin Sans",sans-serif}
.banner .cta span{color:var(--hot)}

/* services */
.svc-title{left:0;top:1765px;width:1200px;text-align:center;font-size:30px}
.svc-sub{left:0;top:1812px;width:1200px;text-align:center;font-size:15px;font-weight:600}
.svc-img{width:188px;height:262px;border-radius:94px;border:1.5px solid var(--hot)}
.svc h4{font-size:27px;line-height:36px;font-weight:500}
.svc p{font-size:12.8px;line-height:18.4px;color:var(--ink-soft);margin-top:6px}
.svc .more{display:inline-block;margin-top:18px;background:var(--hot);color:#fff;font-size:15px;padding:4px 15px;border-radius:6px;font-family:"Josefin Sans",sans-serif}
.svc{width:215px}

/* specialist */
.spec{left:0;top:2640px;width:1200px;height:678px;background:linear-gradient(180deg,#fff,var(--pink-5) 25%,var(--pink-4))}
.spec h2{left:143px;top:155px;font-size:30px}
.spec-img{left:713px;top:155px;width:347px;height:445px;border-radius:173px;border:1.5px solid var(--hot)}

/* footer */
.fnav{left:0;top:3318px;width:1200px;height:72px;background:var(--hot);display:flex;justify-content:center;align-items:center;gap:44px}
.fnav a{color:#fff;font-size:21px;text-decoration:none;font-family:"Josefin Sans",sans-serif}
.plans{left:0;top:3390px;width:1200px;height:140px;background:var(--slate);padding-top:24px}
.plans div{display:flex;justify-content:center;color:#fff;font-size:12px;line-height:26px}
.plans span{padding:0 12px;border-left:1px solid #ddd}
.plans span:first-child{border-left:none}
.plans span::before{content:"✓ ";color:#ddd}
.bottom{left:0;top:3530px;width:1200px;height:76px;background:var(--mist);display:flex;justify-content:center;align-items:center;gap:28px;font-size:13.5px;font-weight:600}
.bottom span{display:flex;align-items:center;gap:8px}
</style>
</head>
<body>

<header class="abs topbar">
  <div class="abs brand"><span class="brand-dot"></span><span class="brand-name">Larkfield OB/GYN</span></div>
  <div class="abs contact" style="left:470px">
    <svg width="18" height="18" viewBox="0 0 24 24" fill="none" stroke="#F5168A" stroke-width="2"><path d="M5 3h4l2 5-3 2a11 11 0 0 0 6 6l2-3 5 2v4a2 2 0 0 1-2 2A17 17 0 0 1 3 5a2 2 0 0 1 2-2z"/></svg>
    <div><small>Have Any Questions?</small>(555) 014-2290</div>
  </div>
  <div class="abs contact" style="left:598px">
    <svg width="18" height="14" viewBox="0 0 24 18" fill="none" stroke="#F5168A" stroke-width="2"><rect x="1" y="1" width="22" height="16" rx="2"/><path d="M1 2l11 8 11-8"/></svg>
    <div><small>Email us</small>admin@larkfieldwomenscare.com</div>
  </div>
  <div class="abs contact" style="left:832px">
    <svg width="16" height="20" viewBox="0 0 20 26" fill="none" stroke="#F5168A" stroke-width="2"><path d="M10 25s8-9 8-15a8 8 0 0 0-16 0c0 6 8 15 8 15z"/><circle cx="10" cy="10" r="3"/></svg>
    <div><small>Our Location</small>4180 Orchard Lane, Suite<br>210, Larkfield, CA 90412</div>
  </div>
  <div class="abs contact" style="left:1040px">
    <svg width="20" height="20" viewBox="0 0 24 24" fill="none" stroke="#F5168A" stroke-width="2"><rect x="2" y="8" width="20" height="13" rx="2"/><path d="M6 8V2h12v6M7 13h2M11 13h2M15 13h2M7 17h10"/></svg>
    <div><small>FAX</small>555-014-2291</div>
  </div>
</header>

<nav class="abs nav">
  <a style="left:83px">Home</a>
  <a style="left:180px">Services ⌄</a>
  <a style="left:323px">Resources ⌄</a>
  <a style="left:485px">About Us</a>
  <a style="left:612px">Contact us</a>
</nav>
<div class="abs book">BOOK APPOINTMENT</div>

<section class="abs hero">
  <svg class="abs" style="left:0;top:0" width="1200" height="620" viewBox="0 0 1200 620">
    <path d="M465 0H1200V560H600C680 420 700 300 640 180C600 100 520 60 465 0Z" fill="#F6C6E0"/>
    <path d="M0 505C250 470 500 490 700 530C900 570 1050 590 1200 575V620H0Z" fill="#fff"/>
    <path d="M0 505C250 470 500 490 700 530C900 570 1050 590 1200 575" stroke="#F5168A" stroke-width="10" fill="none" opacity=".85"/>
    <path d="M0 535C260 495 520 520 720 555C920 585 1060 600 1200 590" stroke="#F1A4CE" stroke-width="8" fill="none"/>
    <path d="M0 580C260 530 500 540 720 575C900 600 1060 612 1200 600" stroke="#F5168A" stroke-width="6" fill="none" opacity=".7"/>
  </svg>
  <h1 class="abs head">Welcome to Larkfield<br>OB/GYN, Larkfield, CA</h1>
  <p class="abs">Lorem ipsum dolor sit amet, consectetur adipiscing elit. Scelerisque viverra nullam.</p>
  <div class="abs" role="img" aria-label="Portrait of a smiling physician in navy scrubs" style="left:660px;top:40px;width:420px;height:470px;border-radius:190px 190px 40px 40px;background:linear-gradient(180deg,rgba(249,217,234,.55),rgba(241,164,206,.35))"></div>
</section>

<section class="intro">
  <div class="abs intro-ring"></div>
  <div class="abs intro-photo photo" role="img" aria-label="Nurse taking a patient's blood pressure"></div>
  <h2 class="abs head">Serving Larkfield Valley<br>Medical Center</h2>
  <div class="abs body-copy" style="left:619px;top:1008px;width:445px">
    <p>At Larkfield OB/GYN in Larkfield, California, we believe better health starts when the patient is educated. For this reason, we take time to listen to our patients concerns, explain each option available, and to answer any questions our patients may have so that they can make informed decisions. At Larkfield OB/GYN, our providers tailor every procedure performed and treatment option recommended to meet the specific needs of our patients. We remain up-to-date on the latest technology and practice guidelines for women's health.</p>
    <p>Our medical providers will take time to give you the personalized health care you deserve. This includes taking time to listen to you and screening you for problems to help ensure that any health issues are diagnosed and treated as early as possible.</p>
  </div>
</section>

<section class="abs banner">
  <div class="abs eyebrow head">Better Health Starts Here!</div>
  <h3 class="abs">Now Accepting New Patients</h3>
  <div class="abs cta"><span>Click Here</span> for an Appointment<br>or Call Us At <span>(555) 014-2290</span></div>
  <div class="abs" style="left:545px;top:110px;width:80px;height:1.5px;background:var(--ink)"></div>
  <div class="abs" role="img" aria-label="Line illustration of a doctor consulting with a pregnant patient" style="left:580px;top:-10px;width:340px;height:265px;border-radius:20px;background:linear-gradient(120deg,rgba(241,164,206,.18),rgba(252,239,246,.08))"></div>
</section>

<h2 class="abs head svc-title">How we can help you?</h2>
<div class="abs svc-sub">Health Services Offered</div>

<div class="abs svc-img photo" role="img" aria-label="Pregnant patient with her sonographer" style="left:138px;top:1882px"></div>
<div class="abs svc" style="left:348px;top:1896px">
  <h4 class="head">Pregnancy Care</h4>
  <p>Receiving regular care in pregnancy is important for the health of both you and your baby. Our obstetricians work with you every step of the way during your pregnancy and delivery to make sure your individual needs are met and co ensure this special journey is a memorable one.</p>
  <span class="more">LEARN MORE</span>
</div>

<div class="abs svc-img photo" role="img" aria-label="Hands holding an ultrasound print" style="left:638px;top:1882px"></div>
<div class="abs svc" style="left:848px;top:1893px;width:215px">
  <h4 class="head">Birth Control</h4>
  <p>Our gynecologists are knowledgeable on all forms of birth control including the IUD, Nexplanon, vaginal ringinsertion, birth control pills, and more! We would love to work with you to determine the best option for you and your lifestyle.</p>
  <span class="more">LEARN MORE</span>
</div>

<div class="abs svc-img photo" role="img" aria-label="Provider checking a patient's blood pressure" style="left:138px;top:2213px"></div>
<div class="abs svc" style="left:348px;top:2226px">
  <h4 class="head">Well Woman<br>Exams</h4>
  <p>Our providers will help you to stay healthy by performing a physical exam on you annually. We will screen you for multiple health conditions that may pose a risk to you. This includes screening you for cancerous conditions of the breast, ovaries and cervix.</p>
  <span class="more">LEARN MORE</span>
</div>

<div class="abs svc-img photo" role="img" aria-label="Doctor examining an expectant mother" style="left:638px;top:2213px"></div>
<div class="abs svc" style="left:848px;top:2228px">
  <h4 class="head">Woman's Health</h4>
  <p>Whether you are dealing with painful or irregular periods, fibroids, or other women's health i ssues, we can help. We offer a variety of the most up-to-date treatment options to help you regain your lifestyle.</p>
  <span class="more">LEARN MORE</span>
</div>

<section class="abs spec">
  <svg class="abs" style="left:0;top:-30px" width="1200" height="150" viewBox="0 0 1200 150">
    <path d="M0 40C300 20 520 60 720 100C900 130 1060 120 1200 95" stroke="#F5168A" stroke-width="9" fill="none" opacity=".85"/>
    <path d="M0 70C280 45 520 80 720 115C900 140 1060 135 1200 115" stroke="#F1A4CE" stroke-width="7" fill="none"/>
    <path d="M0 100C280 70 500 95 700 125C900 150 1060 145 1200 130" stroke="#F5168A" stroke-width="5" fill="none" opacity=".6"/>
  </svg>
  <h2 class="abs head">Your OB/GYN Specialist</h2>
  <div class="abs body-copy" style="left:138px;top:210px;width:478px">
    <p>Larkfield OB/GYN offers you the best care possible in a personalized setting. We are currently accepting patients. Call our office now to make an appointment.</p>
    <p>Larkfield OB/GYN (located near Larkfield Valley Hospital in Larkfield, CA) is a medical office that specializes in Christ-centered healthcare for women of all ages. Our team of exclusively female providers have years of experience taking care of women with a variety of pregnancy and gynecology concerns.</p>
    <p>Whether you need a routine examination, help during your pregnancy, have questions on birth control, or another female concern, we offer the best care possible for our patients. That is why better health starts here.</p>
    <p>Our office provides you with an environment where you can feel comfortable and where you know you will be in good hands. Our providers are leaders women's health. Dr. Halvorsen is a board certified obstetrician and gynecologist. Dr. Marlow is a board eligible obstetrician and gynecologist.</p>
  </div>
  <div class="abs spec-img" role="img" aria-label="Nurse holding a newborn baby" style="background:linear-gradient(165deg,#fff,var(--pink-5))"></div>
</section>

<footer>
  <nav class="abs fnav">
    <a>Home</a><a>About us</a><a>News</a><a>Patient Resources</a><a>Privacy Policy</a><a>Contact us</a>
  </nav>
  <div class="abs plans">
    <div><span>Alderpoint</span><span>Inland Direct</span><span>Primewell of Oakdale</span><span>Primewell of Fairview</span><span>SUMMIT</span><span>Brightpath Oakdale</span><span>Tri-Service Prime</span></div>
    <div><span>Aldera Open Access Select</span><span>Anvil Select</span><span>Blue Harbor</span><span>Cedarline</span><span>Cedarline Local Plus</span><span>Vet Care Plan</span><span>EBSN</span><span>GEPA</span><span>HealthLink West</span></div>
    <div><span>Steel Trades Trust Fund</span><span>Builders Health &amp; Welfare Fund</span><span>Postal Carriers</span><span>Crane Operators</span><span>Metal Trades Guild</span><span>Tri-Service Select</span><span>UnityCare Health</span></div>
    <div><span>GFWU</span><span>UHR</span><span>Primewell of Sun Valley</span></div>
  </div>
  <div class="abs bottom">
    <span><svg width="18" height="18" viewBox="0 0 24 24" fill="none" stroke="#222" stroke-width="2"><path d="M5 3h4l2 5-3 2a11 11 0 0 0 6 6l2-3 5 2v4a2 2 0 0 1-2 2A17 17 0 0 1 3 5a2 2 0 0 1 2-2z"/></svg>(555) 014-2290</span>
    <span><svg width="18" height="14" viewBox="0 0 24 18" fill="none" stroke="#222" stroke-width="2"><rect x="1" y="1" width="22" height="16" rx="2"/><path d="M1 2l11 8 11-8"/></svg>admin@larkfieldwomenscare.com</span>
    <span><svg width="16" height="20" viewBox="0 0 20 26" fill="none" stroke="#222" stroke-width="2"><path d="M10 25s8-9 8-15a8 8 0 0 0-16 0c0 6 8 15 8 15z"/><circle cx="10" cy="10" r="3"/></svg>4180 Orchard Lane, Suite 210, Larkfield, CA 90412</span>
    <span><svg width="18" height="18" viewBox="0 0 24 24" fill="none" stroke="#222" stroke-width="2"><rect x="2" y="8" width="20" height="13" rx="2"/><path d="M6 8V2h12v6M7 13h2M11 13h2M15 13h2M7 17h10"/></svg>555-014-2291</span>
  </div>
</footer>

</body>
</html>
```